Speisekarten-Design für Cafe & Restaurant
Zielgruppe
Cafe & Restaurant, Geöffnet 9-18 uhr, Zielgruppe 60 % über 60 Jahre, 30% 25-50 Jahre und 10% 15-25 Jahre, Einrichtung modern in grün gelblichen pastel tönen, Speisekarten Mappen vorhanden A4 in grau.
Aufgabenstellung
Einhaltung der Speisekarten Schrift : Mark pro , Farbe der Schrift (wahrscheinlich nur bei drucken wichtig) CMYK, Vorhandene Kartenmappe (siehe foto) , wäre vom Vorteil, allerdings sind wir auch für komplett neues design offen. Das 'Vorwort' kann bzw. würde mich freuen , wenn es geändert oder schöner geschrieben wird, leider fehlen uns dafür die Ideen. Bei Fragen einfach mal kurz anschreiben. Danke

```html
<!DOCTYPE html>
<html lang="de">
<head>
<meta charset="utf-8">
<title>Speisekarte – Frühstück & Getränke</title>
<link href="https://fonts.googleapis.com/css2?family=Figtree:wght@400;500;600&display=swap" rel="stylesheet">
<style>
  :root {
    --page: #ffffff;
    --ink: #1d1d1b;
    --title-grey: #9a9a9a;
    --frame-grey: #9d9d9d;
    --breakfast-yellow: #fcfcc5;
    --coffee-beige: #e1c4a9;
    --tea-green: #e1e8a8;
    --illus-grey: #8e8e8e;
    --leaf-green: #a8c41e;
  }
  * { margin: 0; padding: 0; box-sizing: border-box; }
  html, body { width: 848px; height: 1200px; overflow: hidden; background: var(--page); }
  body {
    position: relative;
    font-family: "Figtree", sans-serif;
    color: var(--ink);
    font-size: 18.5px;
    letter-spacing: 0.4px;
  }
  .panel { position: absolute; }
  .panel--breakfast {
    left: 57px; top: 73px; width: 707px; height: 182px;
    background: var(--breakfast-yellow);
    border: 1.5px solid var(--frame-grey);
    border-radius: 16px;
  }
  .panel--hot {
    left: 62px; top: 322px; width: 696px; height: 323px;
    background: var(--coffee-beige);
    border: 2px dashed var(--frame-grey);
  }
  .panel--tea {
    left: 60px; top: 723px; width: 701px; height: 332px;
    background: var(--tea-green);
    border: 1px solid var(--frame-grey);
    border-radius: 16px;
  }
  .panel-title {
    position: absolute;
    transform: translate(-50%, -50%);
    background: var(--page);
    padding: 0 8px;
    font-size: 25px;
    font-weight: 600;
    color: var(--title-grey);
    white-space: nowrap;
    line-height: 1;
    letter-spacing: 1px;
  }
  .line {
    position: absolute;
    line-height: 22px;
    white-space: nowrap;
  }
  .heading { font-weight: 600; }
  .price { text-align: right; }
  sup { font-size: 10px; vertical-align: 8px; margin-left: 2px; }
  .bullet::before {
    content: "•";
    position: absolute;
    left: -17px;
    font-size: 13px;
  }
  .illustration { position: absolute; }
</style>
</head>
<body>

<!-- Frühstück -->
<section class="panel panel--breakfast"></section>
<h2 class="panel-title" style="left:398px; top:74px;">Frühstück</h2>
<p class="line" style="left:76px; top:108px;">2 Semmeln, Butter, Marmelade, Schinken, Käse, Salami, Honig,</p>
<p class="line" style="left:76px; top:142px;">0,1 l&nbsp; Orangensaft&nbsp; + ein heißes Getränk ihrer Wahl<sup>1,2,3,4,5</sup></p>
<p class="line" style="left:76px; top:176px;">(bis 11 Uhr)</p>
<p class="line" style="left:76px; top:209px;">6,70 €</p>

<!-- Heiße Getränke -->
<section class="panel panel--hot"></section>
<h2 class="panel-title" style="left:417px; top:322px;">Heiße Getränke</h2>

<p class="line heading" style="left:81px; top:356px;">Kaffeespezialitäten</p>
<p class="line" style="left:81px; top:389px;">Tasse Kaffee<sup>7</sup></p>
<p class="line price" style="left:262px; width:80px; top:389px;">1,70 €</p>
<p class="line" style="left:81px; top:423px;">Haferl Kaffee<sup>7</sup></p>
<p class="line price" style="left:262px; width:80px; top:423px;">2,10 €</p>
<p class="line" style="left:81px; top:456px;">Portion Kaffee<sup>7</sup></p>
<p class="line price" style="left:262px; width:80px; top:456px;">2,80 €</p>
<p class="line" style="left:81px; top:490px;">Espresso<sup>7</sup></p>
<p class="line price" style="left:262px; width:80px; top:490px;">1,90 €</p>
<p class="line" style="left:81px; top:523px;">Cappuccino<sup>7</sup></p>
<p class="line price" style="left:262px; width:80px; top:523px;">2,20 €</p>
<p class="line" style="left:81px; top:557px;">Latte Macchiato<sup>7</sup></p>
<p class="line price" style="left:262px; width:80px; top:557px;">2,60 €</p>
<p class="line" style="left:81px; top:590px;">Haferl Milchkaffee<sup>7</sup></p>
<p class="line price" style="left:262px; width:80px; top:590px;">2,60 €</p>

<p class="line heading" style="left:380px; top:356px;">Schokoladen</p>
<p class="line" style="left:380px; top:389px;">Schokoladen</p>
<p class="line price" style="left:657px; width:80px; top:389px;">2,60 €</p>
<p class="line" style="left:380px; top:423px;">Heiße Schokolade mit Sahne</p>
<p class="line price" style="left:657px; width:80px; top:423px;">2,80 €</p>
<p class="line" style="left:380px; top:456px;">Heiße Weiße Schokolade<sup>7</sup></p>
<p class="line price" style="left:657px; width:80px; top:456px;">2,80 €</p>
<p class="line" style="left:380px; top:490px;">Heiße Weiße Schokolade</p>
<p class="line" style="left:380px; top:523px;">mit Espresso<sup>7</sup></p>
<p class="line price" style="left:657px; width:80px; top:523px;">3,50 €</p>

<div class="illustration" role="img" aria-label="Illustration einer dampfenden Kaffeetasse"
     style="left:582px; top:566px; width:95px; height:92px; border-radius:40% 40% 50% 50%; background:radial-gradient(circle at 50% 70%, #b9b9b9, rgba(225,196,169,0) 70%);"></div>

<!-- Teespezialitäten -->
<section class="panel panel--tea"></section>
<h2 class="panel-title" style="left:417px; top:721px;">Teespezialitäten</h2>

<p class="line" style="left:85px; top:763px;">Glas Tee</p>
<p class="line" style="left:250px; top:763px;">2,20 €</p>
<p class="line" style="left:85px; top:797px;">Loser Tee aus ökologischem Fairtrade Anbau serviert</p>
<p class="line" style="left:85px; top:830px;">im Glaskännchen&nbsp; 3,50 €</p>

<p class="line bullet" style="left:104px; top:864px;">Darjeeling Royal</p>
<p class="line bullet" style="left:104px; top:897px;">Feiner und milder<br>&nbsp;schwarzer Tee</p>
<p class="line bullet" style="left:104px; top:953px;">Grüntee China Blatt</p>
<p class="line bullet" style="left:104px; top:987px;">Weicher, zartsüsser<br>&nbsp;unfermentierter Tee</p>

<p class="line bullet" style="left:369px; top:864px;">Rooibos Vanilla</p>
<p class="line bullet" style="left:369px; top:897px;">Südafrikanischer Rotbusch, mildes Aroma</p>
<p class="line bullet" style="left:369px; top:931px;">Früchtegarten</p>
<p class="line bullet" style="left:369px; top:964px;">Komposition aus Hibiskus,<br>&nbsp;Sonnenblumenblüten, Apfel,<br>&nbsp;Hagebutten und Zitrus</p>

<div class="illustration" role="img" aria-label="Illustration einer Teeschale mit Löffel und grünen Teeblättern"
     style="left:651px; top:997px; width:100px; height:80px; border-radius:30% 30% 50% 50%; background:radial-gradient(circle at 60% 40%, #b7cf4a, #c4c4c4 55%, rgba(225,232,168,0) 75%);"></div>

</body>
</html>
```